Simple HVAC & Electrical Contractor Billboard

Leasing a 12'3" H by 49'3" W billboard. I'd like to use our current logo and add a few words to let people know what we do. Looking for a clean simple look.
Our company name is Harold Pruett Mechanical - What we are is Air Conditioning & Electrical Contractors.

Our license numbers are TACLA00052916K & TECL71420 they will need to be visible on the sign somewhere.

I'm not sure how much information I want to see on the sign. I want to keep it clean but some of our contact info is as follows. Office # 555-208-4619 - Webpage hpmexample.com. I feel like most people can search the name to find the contact info they need but I'll defer to the designers to come up with the best design.

I have attached a couple different logos we have used I the past.

```html
<!DOCTYPE html>
<html lang="en">
<head>
<meta charset="utf-8">
<title>Harold Pruett Mechanical Billboard</title>
<link rel="stylesheet" href="https://fonts.googleapis.com/css2?family=Lato:wght@400;700&family=Montserrat:wght@700&display=swap">
<style>
  :root {
    --page: #ffffff;
    --board: #ffffff;
    --ink: #333132;
    --red: #ee3338;
    --guide: #f08a8c;
  }
  * { margin: 0; padding: 0; box-sizing: border-box; }
  html, body { width: 1200px; height: 1000px; overflow: hidden; background: var(--page); }
  .canvas { position: relative; width: 1200px; height: 1000px; }
  .billboard {
    position: absolute; left: 168px; top: 392px;
    width: 864px; height: 215px;
    background: var(--board);
    box-shadow: 0 2px 8px rgba(0,0,0,0.35);
    overflow: hidden;
  }
  .billboard-shapes { position: absolute; inset: 0; }
  .brand {
    position: absolute; left: 24px; top: 24px; width: 230px;
    display: flex; flex-direction: column; align-items: center;
  }
  .brand-square { width: 56px; height: 56px; background: var(--red); margin-bottom: 12px; }
  .brand-name {
    font-family: "Lato", sans-serif; font-weight: 700;
    color: var(--ink); font-size: 24px; line-height: 26px;
    text-align: center; text-transform: uppercase; letter-spacing: 0.5px;
  }
  .message { position: absolute; left: 425px; top: 56px; }
  .headline {
    font-family: "Montserrat", sans-serif; font-weight: 700;
    font-size: 36px; line-height: 40px; color: var(--ink); letter-spacing: 0.3px;
  }
  .subhead {
    font-family: "Lato", sans-serif; font-weight: 700;
    font-size: 28px; line-height: 30px; color: var(--red); text-transform: uppercase;
  }
  .contact, .licenses {
    font-family: "Lato", sans-serif; font-size: 16.5px; line-height: 20px; color: var(--ink);
  }
  .contact { font-weight: 700; }
  .contact .accent { color: var(--red); }
  .licenses { font-weight: 400; }
</style>
</head>
<body>
<div class="canvas">
  <section class="billboard">
    <svg class="billboard-shapes" width="864" height="215" viewBox="0 0 864 215">
      <g class="guides" stroke="var(--guide)" stroke-width="1" stroke-dasharray="3 3" fill="none">
        <line x1="218" y1="25" x2="288" y2="25"/>
        <line x1="327" y1="36" x2="327" y2="110"/>
        <line x1="25" y1="168" x2="25" y2="205"/>
      </g>
      <polygon class="bar-top" points="259,0 279,0 279,48 259,68" fill="var(--ink)"/>
      <polygon class="bar-bottom" points="0,196 130,196 112,215 0,215" fill="var(--ink)"/>
      <path class="frame" d="M425,19 L864,19 M361,47 L301,108 L389,197 L864,197" stroke="var(--ink)" stroke-width="6" fill="none"/>
      <polygon class="tab-top" points="319,0 402,0 432,29 389,72" fill="var(--red)"/>
      <g class="pin-icon" fill="none" stroke="#fff" stroke-width="1.5">
        <circle cx="394" cy="30" r="11"/>
        <path d="M394,37 C390,32 389,30 389,27 A5,5 0 0 1 399,27 C399,30 398,32 394,37 Z"/>
        <circle cx="394" cy="27" r="1.6"/>
      </g>
      <polygon class="tab-bottom" points="190,215 292,113 382,205 372,215" fill="var(--red)"/>
      <line x1="250" y1="168" x2="300" y2="150" stroke="#fff" stroke-width="1" stroke-dasharray="3 3"/>
      <g class="up-icon" fill="none" stroke="#fff" stroke-width="2.2">
        <polyline points="240,190 246,184 252,190"/>
        <polyline points="240,197 246,191 252,197"/>
      </g>
    </svg>
    <div class="brand">
      <div class="brand-square"></div>
      <div class="brand-name">Harold Pruett<br>Mechanical</div>
    </div>
    <div class="message">
      <h1 class="headline">AIR CONDITIONING</h1>
      <h2 class="subhead">&amp; Electrical Contractors</h2>
      <p class="contact">Office <span class="accent"># 555-208-4619</span> - Webpage <span class="accent">hpmexample.com</span></p>
      <p class="licenses">license numbers: TACLA00052916K &amp; TECL71420</p>
    </div>
  </section>
</div>
</body>
</html>
```